Marvantar - Seafood industry professional promoting page

Hi. I´m in the seafood business with a one man company sourcing and exporting frozen seafood. I need to make a one page homepage for Marvantar (from Iceland). The feeling of it should be; Trustworthy, experience and knowledge.
Using as background a picture (or part of it), or a moving video:

http://www1.brelvik.is/sjorinn/myndir/ufsinn.jpg
https://clipvera.com/583720415

Main text to be:

- We can help source, market and add value to your seafood business
- Years of experience in seafood trade and production
- Extensive knowledge of fishing, seasonality, production and accreditations

Contact:
dagur@marvantar.is
Tel: +3654170392
(with a photo)

p.s. please also make logo look better.

Target Market(s)

Seafood industry

Industry/Entity Type

Business

Logo Text

Marvantar

Coding

Coded - Design and coding required

Number of Pages Required

1 page

Colors
0792cd
33a6d7

```html
<!DOCTYPE html>
<html lang="en">
<head>
<meta charset="utf-8">
<title>Marvantar – Sourcing and Exporting Seafood</title>
<link rel="stylesheet" href="https://fonts.googleapis.com/css2?family=Cinzel:wght@400;700&family=Lora:wght@400;700&display=swap">
<style>
:root{
  --navy:#1b3561;
  --ink:#0f1f5c;
  --sea-deep:#245f8e;
  --sea-mid:#2d84b0;
  --sea-light:#56a8cc;
  --accent:#2b8cbf;
  --foot:#55abcd;
  --tint:#e9f1f8;
  --page:#f6f7f8;
  --grey:#9a9a9a;
  --text:#555;
  --red:#d8312d;
}
*{box-sizing:border-box;margin:0;padding:0}
html,body{width:690px;height:1200px;overflow:hidden}
body{background:var(--page);position:relative;font-family:'Lora',serif;color:var(--text)}
.hero-photo{position:absolute;left:0;top:0;width:690px;height:352px;
  background:radial-gradient(ellipse at 65% 20%,#5cc0ea 0%,#2a9ad0 40%,#1673a8 100%)}
.site-header{position:absolute;left:75px;top:11px;width:535px;height:39px;background:var(--navy);
  display:flex;align-items:center;padding:0 10px}
.brand{display:flex;align-items:center;gap:7px}
.brand-mark{width:10px;height:10px;background:#fff}
.brand-name{font-family:'Cinzel',serif;font-weight:700;color:#fff;font-size:14px;letter-spacing:.5px}
.brand-tag{border-left:1px solid #fff;padding-left:5px;color:#fff;font-size:4.5px;line-height:6px;font-family:'Cinzel',serif;font-weight:700}
.nav{margin-left:auto;display:flex;gap:2px}
.nav a{font-family:'Cinzel',serif;color:#fff;text-decoration:none;font-size:6.5px;padding:8px 9px}
.nav a.active{background:#2a5b86}
.hero-title{position:absolute;left:96px;top:86px;width:244px;height:104px;background:rgba(40,80,120,.45);
  font-family:'Cinzel',serif;font-weight:700;color:#fff;font-size:18.5px;line-height:26px;padding-top:1px}
.hero-btn{position:absolute;left:96px;top:197px;width:46px;height:18px;background:#fff;border-radius:2px;
  font-size:6px;color:#333;display:flex;align-items:center;justify-content:center}
.services{position:absolute;left:75px;top:259px;width:540px;height:178px;display:flex}
.service{flex:1;color:#fff;text-align:center;padding-top:20px}
.service:nth-child(1){background:var(--sea-deep)}
.service:nth-child(2){background:var(--sea-mid)}
.service:nth-child(3){background:var(--sea-light)}
.service svg{width:40px;height:36px}
.service h3{font-family:'Cinzel',serif;font-weight:400;font-size:12px;line-height:14.5px;margin-top:12px}
.dots{font-size:8px;line-height:10px;letter-spacing:1px}
.service p{font-size:5.6px;line-height:9.6px;padding:0 18px;margin-top:2px}
.welcome{position:absolute;left:75px;top:437px;width:540px;height:145px;background:#fff}
.welcome h2{position:absolute;left:0;width:360px;top:19px;text-align:center;font-family:'Cinzel',serif;font-weight:700;color:var(--ink);font-size:14px}
.welcome .red-dots{position:absolute;left:0;width:360px;top:35px;text-align:center;color:var(--red);font-size:8px}
.welcome p{position:absolute;left:22px;width:320px;top:50px;text-align:center;font-size:6px;line-height:12.2px;color:#aaa}
.logo-tile{position:absolute;left:362px;top:17px;width:163px;height:110px;background:#fff;border:3px solid #eee;
  display:flex;align-items:center;justify-content:center;gap:8px}
.logo-tile .sq{width:18px;height:18px;background:var(--ink)}
.logo-tile span{font-family:'Cinzel',serif;font-weight:700;font-size:20px;color:var(--ink)}
.why h2{position:absolute;left:0;width:690px;top:603px;text-align:center;font-family:'Cinzel',serif;font-weight:700;color:var(--ink);font-size:15px}
.stat{position:absolute;top:652px;width:130px;text-align:center}
.stat .num{font-family:'Cinzel',serif;color:var(--accent);font-size:24px;line-height:28px}
.stat .label{font-family:'Cinzel',serif;font-weight:700;color:var(--ink);font-size:11.5px;line-height:15px;margin-top:1px}
.stat .rule{width:56px;height:1px;background:#ddd;margin:7px auto 6px}
.stat p{font-size:5.6px;line-height:9.6px;color:#666;padding:0 6px}
.contact-strip{position:absolute;left:75px;top:786px;width:540px;height:66px;background:#fff}
.contact-item{position:absolute;top:17px;display:flex;gap:14px;align-items:flex-start}
.contact-item svg{width:24px;height:22px;margin-top:5px}
.contact-item small{display:block;font-size:5.6px;color:#666}
.contact-item b{display:block;font-weight:400;font-size:8px;color:#777;margin-top:3px;font-family:'Cinzel',serif}
.message{position:absolute;left:75px;top:852px;width:540px;height:294px;background:var(--tint)}
.message h2{position:absolute;left:0;width:540px;top:22px;text-align:center;font-family:'Cinzel',serif;font-weight:700;color:var(--ink);font-size:16px}
.message p{position:absolute;left:100px;width:340px;top:59px;text-align:center;font-size:5.6px;line-height:9.6px;color:#666}
.field{position:absolute;background:#e3edef;border:1px solid #cfdde0;font-size:5.3px;color:#999;padding:4px 4px}
.send{position:absolute;left:239px;top:231px;width:59px;height:16px;background:var(--accent);color:#fff;border-radius:2px;
  font-size:5.6px;font-weight:700;display:flex;align-items:center;justify-content:center}
.site-footer{position:absolute;left:75px;top:1146px;width:540px;height:42px;background:var(--foot);color:#fff;
  font-family:'Cinzel',serif;font-size:8.5px;display:flex;align-items:center;justify-content:center}
</style>
</head>
<body>
<div class="hero-photo" role="img" aria-label="Underwater photo of a school of fish in blue water"></div>

<header class="site-header">
  <div class="brand">
    <div class="brand-mark"></div>
    <span class="brand-name">MARVANTAR</span>
    <span class="brand-tag">SOURCING AND<br>EXPORTING SEAFOOD</span>
  </div>
  <nav class="nav">
    <a class="active">Home</a><a>About Us</a><a>Contact Us</a>
  </nav>
</header>

<h1 class="hero-title">We can help source, market and add value to your seafood business</h1>
<div class="hero-btn">View more</div>

<section class="services">
  <div class="service">
    <svg viewBox="0 0 40 36" fill="none" stroke="#fff" stroke-width="1.6"><path d="M4 14c6-5 12-5 18 0s12 5 18 0M4 22c6-5 12-5 18 0s12 5 18 0"/></svg>
    <h3>Sourcing<br>Seafood</h3>
    <div class="dots">...</div>
    <p>Etiam ullamcorper. Suspendisse a pellentesque dui, non felis. Maecenas malesuada elit lectus felis, malesuada ultricies. Curabitur et ligula. Ut molestie a, ultricies porta.</p>
  </div>
  <div class="service">
    <svg viewBox="0 0 40 36" fill="none" stroke="#fff" stroke-width="1.6"><circle cx="20" cy="18" r="16"/><path d="M9 20h22l-3 5H12z" fill="#fff"/><rect x="15" y="14" width="10" height="5" fill="#fff"/></svg>
    <h3>Exporting<br>Seafood</h3>
    <div class="dots">...</div>
    <p>Etiam ullamcorper. Suspendisse a pellentesque dui, non felis. Maecenas malesuada elit lectus felis, malesuada ultricies. Curabitur et ligula. Ut molestie a, ultricies porta.</p>
  </div>
  <div class="service">
    <svg viewBox="0 0 40 36" fill="none" stroke="#fff" stroke-width="1.6"><rect x="3" y="5" width="34" height="26" rx="2"/><circle cx="12" cy="15" r="3"/><path d="M7 25c1-4 9-4 10 0M21 13h12M21 18h12M21 23h12"/></svg>
    <h3>Contact<br>Us</h3>
    <div class="dots">...</div>
    <p>Etiam ullamcorper. Suspendisse a pellentesque dui, non felis. Maecenas malesuada elit lectus felis, malesuada ultricies. Curabitur et ligula. Ut molestie a, ultricies porta.</p>
  </div>
</section>

<section class="welcome">
  <h2>Welcome to Marvantar</h2>
  <div class="red-dots">...</div>
  <p>Ut molestie a, ultricies porta urna. Vestibulum commodo volutpat a, convallis ac, laoreet enim. Phasellus fermentum in, dolor. Pellentesque facilisis. Nulla imperdiet sit amet magna. Vestibulum dapibus, mauris nec malesuada fames ac turpis velit, rhoncus eu, luctus et interdum adipiscing wisi. Aliquam erat ac ipsum. Integer aliquam purus. Quisque lorem tortor fringilla sed, vestibulum id.</p>
  <div class="logo-tile"><div class="sq"></div><span>MARVANTAR</span></div>
</section>

<section class="why">
  <h2>WHY PEOPLE CHOOSE US</h2>
  <div class="stat" style="left:84px"><div class="num">400</div><div class="label">COUNTRIES</div><div class="rule"></div><p>We ship our seafood to over 250 countries in the world.</p></div>
  <div class="stat" style="left:214px"><div class="num">5000</div><div class="label">SEAFOOD</div><div class="rule"></div><p>We ship over 5000 seafood every week</p></div>
  <div class="stat" style="left:345px"><div class="num">9518</div><div class="label">HAPPY CLIENTS</div><div class="rule"></div><p>Our clints are always happy with our seafood.</p></div>
  <div class="stat" style="left:476px"><div class="num">21</div><div class="label">YEARS OF<br>EXPERIENCE</div><div class="rule"></div><p>We have 21 years of vast knowledge of experience in exporting seafood</p></div>
</section>

<section class="contact-strip">
  <div class="contact-item" style="left:20px">
    <svg viewBox="0 0 24 22" fill="none" stroke="var(--accent)" stroke-width="1.4"><rect x="1" y="4" width="22" height="14"/><path d="M1 4l11 9 11-9"/></svg>
    <div><small>Have any questions?</small><b>NOREPLY@MARVANTAR.COM</b></div>
  </div>
  <div class="contact-item" style="left:281px">
    <svg viewBox="0 0 24 22" fill="none" stroke="var(--accent)" stroke-width="1.4"><path d="M12 2c6 0 10 3.5 10 8s-4 8-10 8c-1.5 0-3-.2-4-.6L3 20l1.5-4C3 14.5 2 12.3 2 10c0-4.5 4-8 10-8z"/></svg>
    <div><small>Call us</small><b style="font-family:'Lora',serif">+61 (0) 3 5120 4478</b></div>
  </div>
</section>

<section class="message">
  <h2>Send us a message</h2>
  <p>Lorem ipsum dolor sit amet, consectetur adipisicing elit, sed do eiusmod tempor incididunt ut labore et dolore magna alm accusantium doloremque laudantium, totam rem aperiam, eaque ipsequi nesciunt.</p>
  <div class="field" style="left:104px;top:103px;width:163px;height:16px">Your name</div>
  <div class="field" style="left:273px;top:103px;width:163px;height:16px">Your e-mail</div>
  <div class="field" style="left:104px;top:124px;width:332px;height:16px">Subject</div>
  <div class="field" style="left:104px;top:144px;width:332px;height:82px">Message</div>
  <div class="send">Send A Message</div>
</section>

<footer class="site-footer">© 2018 MARVANTAR SEAFOOD</footer>
</body>
</html>
```